Poster for a vegan café with a funny message about the food served.

Design a poster with the text "Eating here was a big missed stake!" for a café at a meditation center (dalvikorsten.se).

```html
<!DOCTYPE html>
<html lang="en">
<head>
<meta charset="utf-8">
<title>Dalvikorsten Café Poster</title>
<link rel="stylesheet" href="https://fonts.googleapis.com/css2?family=Lato:wght@400;900&display=swap">
<style>
  :root {
    --backdrop: #6a6a6a;
    --paper: #f6f6f6;
    --paper-shade: #e9e9e9;
    --ink: #151515;
    --brand-grey: #4a4a4a;
    --accent: #f7bb00;
    --art-light: #f2eee9;
    --art-warm: #e7ddd1;
  }
  * { margin: 0; padding: 0; box-sizing: border-box; }
  html, body {
    width: 1200px;
    height: 2288px;
    overflow: hidden;
    background: var(--backdrop);
  }
  .poster {
    position: absolute;
    left: 60px;
    top: 425px;
    width: 726px;
    height: 966px;
    transform: scale(1.4876);
    transform-origin: 0 0;
    background:
      linear-gradient(135deg, transparent 0 52%, rgba(255,255,255,.7) 52% 60%, transparent 60%),
      linear-gradient(135deg, var(--paper) 0%, #ffffff 45%, var(--paper-shade) 100%);
    box-shadow: 0 18px 30px rgba(0,0,0,.35);
    font-family: "Lato", sans-serif;
  }
  .brand {
    position: absolute;
    left: 244px;
    top: 36px;
    display: flex;
    align-items: center;
    gap: 14px;
  }
  .brand-dot {
    width: 78px;
    height: 78px;
    border-radius: 50%;
    background: var(--accent);
  }
  .brand-name {
    color: var(--brand-grey);
    font-weight: 400;
    font-size: 40px;
    line-height: 46px;
    letter-spacing: 1px;
  }
  .headline {
    position: absolute;
    left: 186px;
    top: 142px;
    width: 360px;
    text-align: center;
    color: var(--ink);
  }
  .headline-line {
    display: block;
    font-weight: 400;
    font-size: 72px;
    line-height: 86px;
    letter-spacing: -2px;
  }
  .headline-missed,
  .headline-stake {
    display: block;
    font-weight: 900;
    font-size: 92px;
    line-height: 82px;
    letter-spacing: -2px;
  }
  .headline-missed { color: var(--accent); margin-top: 2px; }
  .headline-stake { color: var(--ink); }
  .illustration {
    position: absolute;
    left: 103px;
    top: 503px;
    width: 525px;
    height: 425px;
    background: linear-gradient(180deg, var(--art-light) 0%, var(--art-warm) 100%);
  }
</style>
</head>
<body>
  <main class="poster">
    <div class="brand">
      <span class="brand-dot"></span>
      <div class="brand-name">DALVIK<br>ORSTEN</div>
    </div>
    <h1 class="headline">
      <span class="headline-line">Eating Here</span>
      <span class="headline-line">Was A Big</span>
      <span class="headline-missed">MISSED</span>
      <span class="headline-stake">STAKE!</span>
    </h1>
    <div class="illustration" role="img" aria-label="Illustration of a barista in a purple apron sitting cross-legged in meditation, surrounded by a circle of floating coffee beans, cups, a coffee bag, moka pot and milk jug"></div>
  </main>
</body>
</html>
```